Zombie Themed Web Site Design

I am looking for a web page design for a web site that will be selling zombie themed items.

Starting out we are selling one product, a zombie combat patch so I would like the web design to be based of it, but the attached image should only be a starting point. Please do not hesitate to be as creative as possible.

The site design should be family friendly but defiantly be zombie themed. For the color schema it does not have to be the black and reds that the patch is based on for the page theme.

The Home page should be a page of shear zombie awesomeness that points to the products.

That other pages that are to be static, are the:
About Us, Gallery, Refund Policy, Privacy Policy, Terms & Conditions, Shipping and Delivery and Contact us pages.

-LINK- to the web site (there is nothing there yet)
http://ghoulwatchgearworks.com

-LINK- to the zombie patch image
https://www.filecrate.example/s/qm7ktr20vn8pld/Zombie.jpg

PSD file output is just fine, HTML and CSS files are even better.

If there are any questions, please leave a comment.
Updates

From the submission that I have been receiving, I need to clarifyjust what I am looking for. The theme of the site should be less of zombies risingout of the grave and eating people’s brains, and more a group of peoplethat have formed together (a “task force” if that helps) to hunt and kill zombies.I hope that this helps.

-Marcus    

Industry/Entity Type

Shipping

Requirements
Nice to have
• The use of a military font in the design would awsome.

```html
<!DOCTYPE html>
<html lang="en">
<head>
<meta charset="utf-8">
<title>Zombie apocalypse — Home</title>
<link rel="stylesheet" href="https://fonts.googleapis.com/css2?family=Source+Sans+3:wght@400;600;700&family=Anton&display=swap">
<style>
  :root {
    --page-black: #030303;
    --ink-white: #f4f4f4;
    --ink-dark: #2b2016;
    --orange: #e8702a;
    --orange-deep: #b9501b;
    --orange-light: #f6c26a;
    --nav-brown: #5a3a26;
    --nav-brown-dark: #2a1c14;
    --panel-shade: rgba(5, 5, 8, 0.72);
    --card-border: #3c3f44;
    --scene-top: #3b4652;
    --scene-mid: #1d232b;
    --scene-low: #4a3a2c;
    --field-light: #e8e8e8;
  }
  * { box-sizing: border-box; margin: 0; padding: 0; }
  html, body { width: 1095px; height: 1200px; overflow: hidden; background: var(--page-black); }
  body { position: relative; font-family: "Source Sans 3", Arial, sans-serif; color: var(--ink-white); }

  .site-header { position: absolute; left: 0; top: 0; width: 1095px; height: 130px; }
  .brand { position: absolute; left: 78px; top: 14px; font-weight: 700; font-size: 48px; line-height: 1.05; color: var(--orange); }
  .brand .brand-line2 { display: block; padding-left: 92px; }

  .login { position: absolute; left: 622px; top: 27px; width: 343px; height: 35px; border-radius: 18px;
           background: linear-gradient(#f08a3c, var(--orange-deep)); padding: 5px 8px; display: flex; align-items: center; gap: 12px; }
  .login .field { height: 21px; border-radius: 6px; background: var(--field-light); color: #222; font-size: 14px; text-align: center; line-height: 21px; }
  .login .field-user { width: 115px; }
  .login .field-pass { width: 116px; }
  .login .login-button { width: 71px; height: 19px; border-radius: 10px; background: #050505; color: #fff; font-size: 13px; text-align: center; line-height: 19px; }

  .hero-scene { position: absolute; left: 8px; top: 130px; width: 1079px; height: 994px;
                background: linear-gradient(180deg, var(--scene-top) 0%, var(--scene-mid) 40%, #15181d 60%, var(--scene-low) 88%, #6b5a2a 100%); }

  .main-nav { position: absolute; left: 38px; top: 130px; width: 1013px; height: 50px; border-radius: 10px 10px 0 0;
              background: linear-gradient(var(--nav-brown), var(--nav-brown-dark)); }
  .main-nav a { position: absolute; top: 13px; color: var(--ink-white); text-decoration: none; font-size: 18px; }

  .intro-panel { position: absolute; left: 38px; top: 180px; width: 1013px; height: 434px; background: var(--panel-shade); }
  .intro-text { position: absolute; left: 80px; top: 232px; font-size: 18px; line-height: 37px; color: #fff; white-space: nowrap; }

  .quick-icon { position: absolute; top: 523px; width: 54px; height: 54px; }

  .product-card { position: absolute; top: 676px; width: 320px; height: 307px; border-radius: 14px; border: 6px solid var(--card-border);
                  background: radial-gradient(circle at 35% 5%, #fbe27e 0%, var(--orange-light) 25%, #f0994a 65%, var(--orange) 100%); color: var(--ink-dark); }
  .product-card h2 { position: absolute; left: 30px; top: 20px; font-size: 22px; font-weight: 700; color: #3a2a18; }
  .product-card ul { position: absolute; left: 27px; top: 56px; list-style: none; font-size: 11px; line-height: 22.6px; color: #2a1c10; white-space: nowrap; }
  .product-card .price-label { position: absolute; left: 27px; top: 188px; font-size: 16px; }
  .product-card .price { position: absolute; left: 160px; top: 178px; font-family: "Anton", Impact, sans-serif; font-size: 44px; color: #3a2a1a; }
  .product-card .card-button { position: absolute; left: 67px; top: 250px; width: 164px; height: 28px;
                               background: linear-gradient(90deg, #8a3a14, #d86a2a 50%, #8a3a14); color: #fff; font-weight: 700; font-size: 13px; text-align: center; line-height: 28px; }

  .feature { position: absolute; left: 762px; top: 670px; }
  .feature h3 { font-size: 17px; font-weight: 700; line-height: 21px; color: var(--orange); }
  .feature p { margin-top: 12px; font-size: 12px; line-height: 26.7px; color: #e6e6e6; white-space: nowrap; }
  .feature-price { position: absolute; left: 956px; top: 904px; font-family: "Anton", Impact, sans-serif; font-size: 42px; line-height: 1.2; color: #fff; }
  .feature-button { position: absolute; left: 764px; top: 1038px; width: 146px; height: 39px; background: linear-gradient(#e8702a, #b24a18);
                    color: #fff; font-weight: 700; font-size: 16px; text-align: center; line-height: 39px; }

  .closing-text { position: absolute; left: 35px; top: 1008px; font-size: 15px; line-height: 25px; color: #f0f0f0; white-space: nowrap; }

  .footer-band { position: absolute; left: 0; top: 1095px; width: 1095px; height: 29px; background: linear-gradient(rgba(60,60,40,0.5), rgba(0,0,0,0.8)); }
  .site-footer { position: absolute; left: 0; top: 1124px; width: 1095px; height: 76px; background: var(--page-black); }
  .site-footer a { position: absolute; top: 27px; color: #fff; text-decoration: none; font-size: 16px; transform: translateX(-50%); }
</style>
</head>
<body>
  <header class="site-header">
    <div class="brand">Zombie<span class="brand-line2">apocalypse</span></div>
    <form class="login">
      <div class="field field-user">Username</div>
      <div class="field field-pass"></div>
      <div class="login-button">LOGIN</div>
    </form>
  </header>

  <div class="hero-scene" role="img" aria-label="Illustrated street scene at dusk with a zombie-hunting task force in front of houses and fallen zombies below"></div>

  <nav class="main-nav">
    <a href="#" style="left:53px">Home</a>
    <a href="#" style="left:205px">Gallery</a>
    <a href="#" style="left:364px">About Us</a>
    <a href="#" style="left:548px">Shipping and Delivery</a>
    <a href="#" style="left:857px">Contact</a>
  </nav>

  <section class="intro-panel"></section>
  <p class="intro-text">Lorem ipsum dolor sit amet, consectetuer adipiscing elit, sed<br>diam nonummy nibh euismod tincidunt ut laoreet dolore<br>magna aliquam erat volutpat. Ut wisi enim ad minim<br>veniam, quis nostrud exerci tation ullamcorper suscipit<br>lobortis nisl ut aliquip ex ea commodo. &nbsp;Duis autem vel eum<br>iriure dolor in hendrerit in vulputate velit esse molestie<br>consequat, vel illum dolore eu feugiat nulla facilisis at vero</p>

  <svg class="quick-icon" style="left:280px" viewBox="0 0 54 54" aria-label="Email">
    <circle cx="27" cy="27" r="27" fill="#3a2416"/>
    <rect x="13" y="18" width="28" height="18" fill="#fff"/>
    <path d="M13 18 L27 29 L41 18" fill="none" stroke="#3a2416" stroke-width="2"/>
  </svg>
  <svg class="quick-icon" style="left:382px" viewBox="0 0 54 54" aria-label="Cart">
    <circle cx="27" cy="27" r="27" fill="#3a2416"/>
    <path d="M12 17 H17 L21 32 H38 L41 21 H19" fill="none" stroke="#fff" stroke-width="2.5"/>
    <circle cx="23" cy="38" r="2.5" fill="#fff"/><circle cx="36" cy="38" r="2.5" fill="#fff"/>
  </svg>

  <article class="product-card" style="left:37px">
    <h2>Product 2:</h2>
    <ul>
      <li>Lorem ipsum dolor sit amet ipsum dolor sit amet</li>
      <li>Lorem ipsum ipsum dolor sit amet</li>
      <li>Lorem ipsuipsum dolor sit ametm dolor sit amet</li>
      <li>Lorem ipsum dolor ipsum dolor sit amet</li>
      <li>Lorem ipsum dolor sit amet</li>
    </ul>
    <span class="price-label">Lorem ipsum</span>
    <span class="price">$36.00</span>
    <a class="card-button">LOREM IPSUM</a>
  </article>

  <article class="product-card" style="left:395px">
    <h2>Product 3 :</h2>
    <ul>
      <li>Lorem ipsum dolor sit amet ipsum dolor sit amet</li>
      <li>Lorem ipsum ipsum dolor sit amet</li>
      <li>Lorem ipsuipsum dolor sit ametm dolor sit amet</li>
      <li>Lorem ipsum dolor ipsum dolor sit amet</li>
      <li>Lorem ipsum dolor sit amet</li>
    </ul>
    <span class="price-label">Lorem ipsum</span>
    <span class="price">$55.00</span>
    <a class="card-button">LOREM IPSUM</a>
  </article>

  <aside class="feature">
    <h3>Lorem ipsum dolor amet<br>ipsum dolor amet et</h3>
    <p>Lorem ipsum dolor sit amet, consectetuer<br>adipiscing elit, sed diam nonummy nibh<br>euismod tincidunt ut laoreet dolore magna<br>aliquam erat volutpat. Ut wisi enim ad minim<br>veniam, quis nostrud exerci tation<br>suscipit lobortis nisl ut aliquip<br>consequat. Duis autem vel eu<br>hendrerit in vulputate velit ess<br>consequat, vel illum dolore eu<br>feugiat nos et accums<br>iusto odio dignissim qui praesent</p>
  </aside>
  <span class="feature-price">$55.00</span>
  <a class="feature-button">Lorem ipsum</a>

  <p class="closing-text">Lorem ipsum dolor sit amet, consectetuer adipiscing elit, sed diam nonummy nibh euismod tincidunt<br>ut laoreet dolore magna aliquam erat volutpat. Ut wisi enim ad minim veniam, quis nostrud exerci<br>tation ullamcorper suscipit lobortis nisl ut aliquip ex ea commodo. Duis autem vel eum iriure dolor in</p>

  <div class="footer-band"></div>
  <footer class="site-footer">
    <a href="#" style="left:245px">Privacy Policy</a>
    <a href="#" style="left:518px">Refund Policy</a>
    <a href="#" style="left:865px">Terms &amp; Conditions</a>
  </footer>
</body>
</html>
```